PawNook business card

Looking for a fun and cool biz card for a new company with patent pending products. I have products to help and protect dogs hearing. My colors are pantone blue and orange.
Updates

Please add tag line: Protect the ones you love...even your PawNooks!

Target Market(s)

Animal/Dog lovers!

Industry/Entity Type

Retail

Contact Information for Business Card

I'm looking for something simple yet fun with all the info included for biz cards

Colors
0555a3
f78f20

Requirements
Must have
• Logo
Nice to have
• name, website and email
Should not have
• phone number

```html
<!DOCTYPE html>
<html lang="en">
<head>
<meta charset="utf-8">
<title>PawNook Business Card</title>
<link href="https://fonts.googleapis.com/css2?family=Roboto:wght@400;500;700;900&display=swap" rel="stylesheet">
<style>
  :root {
    --backdrop: #3b3430;
    --card: #1f2124;
    --card-front: #17191b;
    --orange: #f5601f;
    --blue: #0555a3;
    --silver: #a9abad;
    --text: #f2f2f2;
    --divider: #8a8c8f;
  }
  * { box-sizing: border-box; margin: 0; padding: 0; }
  html, body { width: 1200px; height: 769px; overflow: hidden; }
  body {
    background: var(--backdrop);
    font-family: "Roboto", Arial, sans-serif;
    position: relative;
  }
  .card {
    position: absolute;
    width: 530px;
    height: 303px;
    border-radius: 3px;
  }
  .card-front {
    left: 50px;
    top: 233px;
    background: var(--card-front);
    display: flex;
    flex-direction: column;
    align-items: center;
    justify-content: center;
    gap: 14px;
  }
  .front-wordmark {
    font-weight: 900;
    font-size: 74px;
    line-height: 1;
    letter-spacing: -2px;
    color: var(--silver);
  }
  .front-tagline {
    font-weight: 400;
    font-size: 16px;
    line-height: 20px;
    color: var(--silver);
  }
  .card-back {
    left: 620px;
    top: 233px;
    background: var(--card);
  }
  .back-wordmark {
    position: absolute;
    left: 28px;
    top: 128px;
    width: 190px;
    text-align: center;
    font-weight: 900;
    font-size: 38px;
    line-height: 46px;
    color: var(--orange);
  }
  .divider {
    position: absolute;
    left: 236px;
    top: 62px;
    width: 1px;
    height: 180px;
    background: var(--divider);
  }
  .contact {
    position: absolute;
    left: 258px;
    top: 82px;
    color: var(--text);
    font-size: 15px;
    line-height: 20px;
  }
  .contact-name {
    color: var(--orange);
    font-weight: 700;
    font-size: 20px;
    line-height: 22px;
    text-transform: uppercase;
  }
  .contact-title {
    color: var(--blue);
    font-weight: 500;
    font-size: 15px;
    text-transform: uppercase;
    margin-bottom: 8px;
  }
  .contact-address { margin-bottom: 6px; }
  .contact-line { display: flex; align-items: center; gap: 8px; }
  .contact-line svg { width: 13px; height: 13px; fill: var(--orange); flex: none; }
</style>
</head>
<body>
  <section class="card card-front">
    <div class="front-wordmark">PawNook</div>
    <div class="front-tagline">Protect the ones you love...even your PawNooks!</div>
  </section>

  <section class="card card-back">
    <div class="back-wordmark">PawNook</div>
    <div class="divider"></div>
    <div class="contact">
      <div class="contact-name">Dana Whitlow</div>
      <div class="contact-title">CEO/Founder</div>
      <div class="contact-address">412 Alder Court<br>Juneau, Alaska 99801</div>
      <div class="contact-line">
        <svg viewBox="0 0 24 24" aria-hidden="true"><path d="M2 5h20v14H2zm2 2v.5l8 5 8-5V7z"/></svg>
        <span>dana@pawnook.com</span>
      </div>
      <div class="contact-line">
        <svg viewBox="0 0 24 24" aria-hidden="true"><path d="M12 2a10 10 0 1 0 0 20 10 10 0 0 0 0-20zm0 2c.9 1.2 1.6 2.6 2 4h-4c.4-1.4 1.1-2.8 2-4zM4.3 14a8 8 0 0 1 0-4h3.4a16 16 0 0 0 0 4zm5.4 0a14 14 0 0 1 0-4h4.6a14 14 0 0 1 0 4zm6.6 0a16 16 0 0 0 0-4h3.4a8 8 0 0 1 0 4zM10 16h4c-.4 1.4-1.1 2.8-2 4-.9-1.2-1.6-2.6-2-4z"/></svg>
        <span>www.pawnook.com</span>
      </div>
    </div>
  </section>
</body>
</html>
```